Fernvale Business Card Design

We are looking for a fresh business card design for our new logo. We would like a business card that is unique but friendly. We are in the window coverings business offering blinds, shutters and shades for homes.

Target Market(s)

Targeting the end-consumer

Industry/Entity Type

Business

Requirements
Must have
• Must have a dedicates space for a photo of our sales person. Must contain our new logo (attached).

```html
<!DOCTYPE html>
<html lang="en">
<head>
<meta charset="utf-8">
<title>Fernvale Business Card</title>
<link href="https://fonts.googleapis.com/css2?family=Arimo:wght@400;700&display=swap" rel="stylesheet">
<style>
  :root{
    --bg:#3a3a3c;
    --card-white:#ffffff;
    --card-fade:#e4e4e4;
    --green:#6aa536;
    --green-text:#72b233;
    --ink:#4a4a4d;
    --band:#55555a;
    --photo-top:#d9dbe0;
    --photo-bottom:#6e7690;
    --back-top:#616165;
    --back-bottom:#4d4d51;
    --back-text:#ececec;
    --rule:#8a8a8e;
  }
  *{margin:0;padding:0;box-sizing:border-box}
  html,body{width:1200px;height:965px;overflow:hidden}
  body{background:var(--bg);font-family:"Arimo",Arial,sans-serif;position:relative}
  .card{position:absolute;left:277px;width:648px;height:369px;overflow:hidden;box-shadow:0 6px 18px rgba(0,0,0,.45)}
  .card--front{top:97px;background:linear-gradient(180deg,var(--card-white) 0%,var(--card-white) 45%,var(--card-fade) 100%)}
  .card--back{top:502px;background:linear-gradient(180deg,var(--back-top),var(--back-bottom))}

  .brand{position:absolute;display:flex;align-items:center}
  .brand__mark{border:4px solid var(--ink);border-radius:6px}
  .brand__name{font-weight:400;letter-spacing:.5px;line-height:1}
  .card--front .brand{left:30px;top:35px}
  .card--front .brand__mark{width:56px;height:56px}
  .card--front .brand__name{font-size:46px;color:var(--ink);margin-left:22px}

  .portrait{position:absolute;left:300px;top:22px;width:254px;height:300px;
    background:linear-gradient(180deg,var(--photo-top) 0%,var(--photo-bottom) 100%)}

  .accent{position:absolute;left:574px;top:228px;width:66px;height:66px;background:var(--green)}

  .wave{position:absolute;left:0;top:0}

  .contact{position:absolute;left:29px;top:0;color:var(--ink)}
  .contact__name{position:absolute;top:140px;font-size:19px;font-weight:700;color:var(--green-text);white-space:nowrap}
  .contact__role{position:absolute;top:164px;font-size:14px;white-space:nowrap}
  .contact__list{position:absolute;top:201px;list-style:none;font-size:14px;line-height:18.5px;white-space:nowrap}
  .contact__label{color:var(--green-text);display:inline-block;width:28px}
  .contact__address{position:absolute;top:270px;font-size:14px;line-height:19px;white-space:nowrap}

  .card--back .brand{left:0;right:0;top:132px;justify-content:center}
  .card--back .brand__mark{width:84px;height:84px;border-color:var(--back-text)}
  .card--back .brand__name{font-size:68px;color:var(--back-text);margin-left:26px}
  .back-url{position:absolute;left:0;right:0;top:333px;display:flex;align-items:center;justify-content:center;gap:20px}
  .back-url__rule{width:160px;height:1px;background:var(--rule)}
  .back-url__text{font-size:13px;letter-spacing:4.5px;color:var(--back-text)}
</style>
</head>
<body>
  <section class="card card--front">
    <div class="portrait" role="img" aria-label="Photo of the sales person"></div>
    <div class="accent" aria-hidden="true"></div>
    <svg class="wave" width="648" height="369" viewBox="0 0 648 369" aria-hidden="true">
      <path d="M0,300 C60,338 130,340 250,318 C380,294 480,284 560,298 C600,306 630,325 648,338 L648,345 C620,330 590,316 540,310 C460,300 380,305 300,318 C180,338 80,346 0,310 Z" fill="var(--band)"/>
      <path d="M0,306 C70,340 150,338 260,320 C380,300 470,298 540,308 C590,316 625,332 648,345 L648,369 L0,369 Z" fill="var(--green)"/>
    </svg>
    <div class="brand">
      <span class="brand__mark"></span>
      <span class="brand__name">Fernvale</span>
    </div>
    <div class="contact">
      <p class="contact__name">Dana Hale</p>
      <p class="contact__role">Founder</p>
      <ul class="contact__list">
        <li><span class="contact__label">P :</span>+032 555 0147</li>
        <li><span class="contact__label">M :</span>info@fernvale.com</li>
        <li><span class="contact__label">W :</span>www.fernvale.com</li>
      </ul>
      <p class="contact__address">Here your company or<br>home address</p>
    </div>
  </section>

  <section class="card card--back">
    <div class="brand">
      <span class="brand__mark"></span>
      <span class="brand__name">Fernvale</span>
    </div>
    <div class="back-url">
      <span class="back-url__rule"></span>
      <span class="back-url__text">www.fernvale.com</span>
      <span class="back-url__rule"></span>
    </div>
  </section>
</body>
</html>
```